Web design for boutique law firm

Web design for law firm; practice areas include:
-international intellectual property counseling
-general corporate (contract negotiation, licensing, distribution agreements
-see my *very* outdated website at www.pvtlegalhouse.com: here is some of the home page content:

"PVT Law Group enjoys providing proactive, business-minded, efficient legal solutions for individuals and companies that benefit from major law firm experience at reasonable rates.

Some areas of emphasis include:

Counseling individuals and companies with respect to clearing, selecting, securing, managing, commercializing, and protecting intellectual property assets around the world. This includes traditional global brand management, marketing, advertising, and enforcement work as well as litigation.
PVT Law Group also provides general counseling services for individuals and businesses, from start-up advice to sophisticated business transactions strategy, agreement negotiating, dispute resolution, and litigation.
Before founding PVT Law Group in 2008, Curtis L. Abernathy led the Trademark, Copyright, & Brand Management Group for Falkner & Ingleby's Seattle office. Curtis was also a senior associate at Silicon Valley based Hartwell, Bexley, Oduya, & Penrose."

Target Market(s)

Clients/potential clients needing tier one, international intellectual property advice with "mega" law firm experience for much less than what we were/would be charging at the "mega firms".

Industry/Entity Type

Legal

Number of Pages Required

4 page

Font styles to use
Serif
Sans Serif

Colors

Designer to choose colors to be used in the design.

Requirements
Must have
• +Improvement over everything on current site at www.pvtlegalhouse.com.
• +Pictures/bios for me and my team (four of us right now).
• +Easy to update and add/remove content.
• +Must be superior in design (look, feel, ease of use, classy and elegant, but hip, reflects international practice).
• +i have logos and color schemes (see current website) but will consider improvements.
Nice to have
• Let me know your thoughts.
Should not have
• No cheese; no overt sales pitches or marketing (since law firm).

```html
<!DOCTYPE html>
<html lang="en">
<head>
<meta charset="utf-8">
<title>PVT Law Group PLLC</title>
<link rel="stylesheet" href="https://fonts.googleapis.com/css2?family=Montserrat:wght@500;600;700&family=Questrial&display=swap">
<style>
:root{
  --backdrop:#e4e4e4;
  --page:#ffffff;
  --ink:#2b2b2b;
  --orange:#d0550f;
  --orange-soft:#e8733f;
  --peach:#f6b892;
  --track:#fcd98a;
  --forest:#1f3c37;
  --night:#0b1119;
  --field:#112038;
  --navy:#0c1330;
  --mint:#3fd39a;
  --pink:#f04bc8;
  --mist:#eef1f5;
  --head:"Montserrat",sans-serif;
  --body:"Questrial",sans-serif;
}
*{box-sizing:border-box;margin:0;padding:0}
html,body{width:1200px;height:3243px;overflow:hidden}
body{background:var(--backdrop);font-family:var(--body);color:var(--ink)}
.page{position:absolute;left:37px;top:43px;width:1126px;height:3157px;background:var(--page);overflow:hidden}
.band{position:absolute;left:0;width:100%}

/* nav */
.site-nav{top:0;height:59px;display:flex;align-items:center;justify-content:space-between;padding:0 24px 0 44px;background:#fff;z-index:5}
.brand{font-family:var(--body);color:var(--orange);font-size:22px;letter-spacing:.5px;border-bottom:2px solid var(--orange);padding-bottom:2px}
.menu{display:flex;gap:20px;list-style:none;font-family:var(--head);font-weight:600;font-size:12px;color:#111;text-transform:uppercase}

/* hero */
.hero{top:59px;height:395px;background:linear-gradient(110deg,#2a1a12 0%,#5a3a26 35%,#3a2a22 60%,#1e1614 100%);clip-path:polygon(0 0,100% 0,100% 84%,0 100%);color:#fff;text-align:center}
.hero h1{font-family:var(--head);font-weight:700;font-size:44px;margin-top:28px}
.hero p{font-size:17px;line-height:1.55;width:700px;margin:24px auto 0}
.btn-learn{display:inline-block;margin-top:26px;width:234px;height:86px;line-height:86px;background:var(--peach);border-radius:8px;font-size:16px;color:#fff;text-transform:uppercase}

/* about */
.about{top:454px;height:560px}
.section-title{font-family:var(--head);font-weight:600;font-size:27px;line-height:34px;text-align:center;color:#111}
.about .section-title{margin-top:0}
.about-left{position:absolute;left:45px;top:44px;width:540px}
.intro{font-size:12.5px;line-height:1.45}
.skill{margin-top:14px}
.skill-label{font-family:var(--head);font-weight:700;font-size:11px;text-transform:uppercase;color:#222;margin-bottom:6px}
.skill-track{height:22px;border-radius:11px;background:var(--track);border:1px solid #d9b86a}
.skill-fill{height:100%;width:85%;border-radius:11px;background:var(--orange)}
.tabs{display:flex;align-items:center;margin-top:48px;gap:0}
.tab{font-family:var(--head);font-weight:600;font-size:12px;color:var(--orange);padding:0 30px}
.tab.active{background:var(--orange);color:#fff;width:130px;height:55px;line-height:55px;text-align:center;border-radius:4px;padding:0}
.history{font-size:12.5px;line-height:1.45;margin-top:14px}
.history + .history{margin-top:16px}
.about-right{position:absolute;left:603px;top:44px;width:476px}
.ceo-photo{position:relative;height:284px;background:linear-gradient(120deg,#a9b4bd 0%,#5b6a78 45%,#1c2230 100%)}
.ceo-overlay{position:absolute;left:0;right:0;bottom:0;height:128px;background:rgba(20,28,48,.7)}
.ceo-portrait{position:absolute;left:24px;bottom:10px;width:112px;height:112px;border-radius:50%;border:4px solid #f3c48e;background:#c9a68a}
.ceo-quote{position:absolute;left:148px;top:176px;right:20px;color:#fff;font-size:11px;line-height:1.35}
.ceo-name{margin-top:12px;font-family:var(--head);font-weight:700;font-size:10px;text-transform:uppercase}
.accordion{list-style:none;margin-top:34px}
.accordion li{height:48px;line-height:46px;background:var(--orange);border:1px solid #6b2a06;color:#fff;font-family:var(--head);font-weight:700;font-size:11px;padding-left:14px;text-transform:uppercase}

/* call to action */
.cta{top:1040px;height:520px;background:linear-gradient(180deg,#d69a62 0%,#c8824d 45%,#b27045 100%);clip-path:polygon(0 14%,100% 0,100% 100%,0 94%);color:#fff;text-align:center}
.cta h2{font-family:var(--head);font-weight:700;font-size:40px;margin-top:142px}
.cta p{font-family:var(--head);font-weight:600;font-size:20px;margin-top:24px}
.btn-contact{display:inline-block;margin-top:26px;width:180px;height:82px;line-height:80px;border:2px solid #fff;border-radius:8px;font-family:var(--head);font-weight:600;font-size:16px}

/* services */
.services{top:1480px;height:360px;background:var(--forest);clip-path:polygon(0 12%,100% 0,100% 100%,0 100%);color:#fff}
.services .section-title{color:#fff;margin-top:62px}
.service-grid{position:absolute;top:118px;left:50px;display:flex;gap:51px}
.service{width:230px;font-size:12px;line-height:1.35}
.service h3{font-family:var(--head);font-weight:600;font-size:15px;text-align:center;margin-bottom:14px}
.service p{height:138px}
.read-more{display:block;text-align:center;color:var(--mint);font-size:12px}

/* testimonial */
.testimonial{top:1815px;height:450px;background:var(--orange-soft);clip-path:polygon(0 0,100% 4%,100% 89%,0 100%);color:#fff}
.testimonial .section-title{color:#fff;margin-top:78px}
.client-photo{position:absolute;left:75px;top:112px;width:190px;height:190px;border-radius:42px;transform:rotate(45deg);background:linear-gradient(160deg,#c9a27a,#efd3bd);border:3px solid #fff}
.quote{position:absolute;left:368px;top:166px;width:665px;font-size:12.5px;line-height:1.45}
.client-name{margin-top:18px;font-family:var(--head);font-weight:700;font-size:12px}
.arrows{position:absolute;left:540px;top:276px;display:flex;gap:50px}

/* contact */
.contact{top:2220px;height:355px;background:var(--night);clip-path:polygon(0 0,100% 2%,100% 100%,0 97%);color:#fff}
.contact .section-title{color:#fff;margin-top:40px}
.field{position:absolute;display:flex;align-items:center;font-size:12.5px}
.field label{width:76px}
.field .input{width:363px;height:37px;background:var(--field)}
.message{position:absolute;left:612px;top:82px;display:flex;font-size:12.5px}
.message label{width:74px;padding-top:4px}
.message .input{width:393px;height:138px;background:var(--field)}
.btn-submit{position:absolute;left:686px;top:238px;width:174px;height:48px;line-height:48px;background:var(--pink);color:#fff;font-size:13px;text-align:center}

/* map */
.map{top:2573px;height:379px;background:linear-gradient(135deg,#ebe7de 0%,#e3ded3 50%,#dfe3e8 100%)}
.map svg{position:absolute;left:722px;top:110px}

/* connect */
.connect{top:2952px;height:140px;background:var(--mist)}
.connect-box{position:absolute;left:245px;top:14px;width:681px;height:112px}
.connect h2{width:510px;margin:0 auto;background:#fff;font-family:var(--head);font-weight:600;font-size:27px;text-align:center;height:50px;line-height:50px;color:#111}
.social{display:flex;justify-content:center;gap:12px;margin-top:14px;list-style:none}
.social li{width:36px;height:36px;border-radius:50%;border:2px solid var(--social)}

/* footer */
.site-footer{top:3098px;height:59px;background:var(--navy);color:#cfd3dc;font-size:10px;text-align:center;line-height:59px;text-transform:uppercase}
</style>
</head>
<body>
<div class="page">

  <header class="band site-nav">
    <span class="brand">PVT LAW GROUP PLLC</span>
    <ul class="menu">
      <li>Home</li><li>About</li><li>Ecperience</li><li>Contact</li>
    </ul>
  </header>

  <section class="band hero" role="img" aria-label="Courtroom still life with gavel and brass scales of justice">
    <h1>A Team of Renowned Attorneys</h1>
    <p>Counseling individuals and companies with respect to clearing, selecting, securing, managing, commercializing, and protecting intellectual property assets around the world. This includes traditional global brand management, marketing, advertising, and enforcement work as well as litigation.</p>
    <span class="btn-learn">Learn More</span>
  </section>

  <section class="band about">
    <h2 class="section-title">About Our Firm</h2>
    <div class="about-left">
      <p class="intro">PVT Law Group enjoys providing proactive, business-minded, efficient legal solutions for individuals and companies that benefit from major law firm experience at reasonable rates.</p>
      <div class="skill"><div class="skill-label">Brand Management</div><div class="skill-track"><div class="skill-fill"></div></div></div>
      <div class="skill"><div class="skill-label">Brand Enforcement</div><div class="skill-track"><div class="skill-fill"></div></div></div>
      <div class="skill"><div class="skill-label">IP Counsel and Management</div><div class="skill-track"><div class="skill-fill"></div></div></div>
      <div class="skill"><div class="skill-label" style="text-transform:none">Litigation</div><div class="skill-track"><div class="skill-fill"></div></div></div>
      <div class="tabs">
        <span class="tab active">History</span><span class="tab">Values</span><span class="tab">Commitment</span>
      </div>
      <p class="history">Before founding PVT Law Group in 2008, Curtis L. Abernathy led the Trademark, Copyright, &amp; Brand Management Group for Falkner &amp; Ingleby's Seattle office. Curtis was also a senior associate at Silicon Valley based Hartwell, Bexley, Oduya, &amp; Penrose.</p>
      <p class="history">Over the years, Curtis has worked with start-ups to Fortune 25 corporations spanning various industries and continues to team with legal professionals in the U.S. and abroad to best serve his clients' needs.</p>
    </div>
    <div class="about-right">
      <div class="ceo-photo" role="img" aria-label="Attorney in a dark suit at a desk reviewing papers">
        <div class="ceo-overlay"></div>
        <div class="ceo-portrait" role="img" aria-label="Portrait of the firm's chief executive"></div>
        <div class="ceo-quote">Lorem Ipsum is simply dummy text of the printing and typesetting industry. Lorem Ipsum has been the industry's standard dummy text ever since the 1500s.
          <div class="ceo-name">Dana Whitlock, CEO</div>
        </div>
      </div>
      <ul class="accordion">
        <li>&gt; Accomplishments</li><li>&gt; Vision</li><li>&gt; Future</li>
      </ul>
    </div>
  </section>

  <section class="band cta" role="img" aria-label="Group of smiling business professionals under a warm orange tint">
    <h2>Have a case that needs resolving?</h2>
    <p>Give us the facts and we'll take care of the rest.</p>
    <span class="btn-contact">Get In Touch Now</span>
  </section>

  <section class="band services">
    <h2 class="section-title">Services Offered</h2>
    <div class="service-grid">
      <article class="service"><h3>Brand Management</h3><p>Managed global brand portfolios for consumer brands, including trademark clearance, prosecution, enforcement, maintenance, sponsorship, licensing, distribution, domain name matters, and litigation/contentious matters.</p><span class="read-more">read more</span></article>
      <article class="service"><h3>Brand Enforcement</h3><p>Established strategy for and resolved complex multi-jurisdictional intellectual property disputes.</p><span class="read-more">read more</span></article>
      <article class="service"><h3>Counterfeiting</h3><p>Coordinated enforcement strategy with consumer electronic client against a S. Korean counterfeiter in coordination with U.S. Customs &amp; Border Protection.</p><span class="read-more">read more</span></article>
      <article class="service"><h3>Litigation</h3><p>Managed litigators, client's relationship and expectations (substantive and fiscal), and assisted with case strategy, in trademark infringement suit that settled for over ten times defendants' initial monetary offer.</p><span class="read-more">read more</span></article>
    </div>
  </section>

  <section class="band testimonial">
    <h2 class="section-title">Testimonial</h2>
    <div class="client-photo" role="img" aria-label="Portrait of the client giving the testimonial"></div>
    <div class="quote">Lorem ipsum dolor sit amet, consectetur adipiscing elit. Nulla nibh ex, cursus eget porta eget, consequat quis nisi. Nullam tincidunt gravida augue nec tempor. Nunc eu velit dictum, dignissim eros quis, consectetur ligula. Cras ac cursus dui, in convallis massa. Mauris pellentesque velit urna, ac vestibulum felis porta sit amet.
      <div class="client-name">Renata Voss</div>
    </div>
    <div class="arrows">
      <svg width="28" height="28" viewBox="0 0 28 28"><path d="M20 4 8 14l12 10" fill="none" stroke="#fff" stroke-width="3"/></svg>
      <svg width="28" height="28" viewBox="0 0 28 28"><path d="M8 4l12 10L8 24" fill="none" stroke="#fff" stroke-width="3"/></svg>
    </div>
  </section>

  <section class="band contact">
    <h2 class="section-title">How to Reach Us</h2>
    <div class="field" style="left:75px;top:82px"><label>Name :</label><span class="input"></span></div>
    <div class="field" style="left:75px;top:138px"><label>Phone :</label><span class="input"></span></div>
    <div class="field" style="left:75px;top:194px"><label>Email :</label><span class="input"></span></div>
    <div class="field" style="left:75px;top:250px"><label>Subject :</label><span class="input"></span></div>
    <div class="message"><label>Message :</label><span class="input"></span></div>
    <span class="btn-submit">Submit</span>
  </section>

  <section class="band map" role="img" aria-label="Street map of the office neighbourhood with a location marker">
    <svg width="40" height="56" viewBox="0 0 40 56"><path d="M20 2C10 2 3 9 3 19c0 13 17 35 17 35s17-22 17-35C37 9 30 2 20 2z" fill="#33475f"/><circle cx="20" cy="19" r="6" fill="#fff"/></svg>
  </section>

  <section class="band connect">
    <div class="connect-box">
      <h2>Let's Stay Connected</h2>
      <ul class="social">
        <li style="--social:#3b5998"></li><li style="--social:#4aa3df"></li><li style="--social:#2c79b3"></li>
        <li style="--social:#c9302c"></li><li style="--social:#d9573f"></li><li style="--social:#e88a2b"></li>
        <li style="--social:#34465d"></li><li style="--social:#2aa8e0"></li>
      </ul>
    </div>
  </section>

  <footer class="band site-footer">© 2008-2017 PVT Law Group PLLC</footer>

</div>
</body>
</html>
```